Web design for boutique law firm

Web design for law firm; practice areas include:
-international intellectual property counseling
-general corporate (contract negotiation, licensing, distribution agreements
-see my *very* outdated website at www.tbkcounsel.com: here is some of the home page content:

"TBK Law Group enjoys providing proactive, business-minded, efficient legal solutions for individuals and companies that benefit from major law firm experience at reasonable rates.

Some areas of emphasis include:

Counseling individuals and companies with respect to clearing, selecting, securing, managing, commercializing, and protecting intellectual property assets around the world. This includes traditional global brand management, marketing, advertising, and enforcement work as well as litigation.
TBK Law Group also provides general counseling services for individuals and businesses, from start-up advice to sophisticated business transactions strategy, agreement negotiating, dispute resolution, and litigation.
Before founding TBK Law Group in 2008, Curtis P. Langford led the Trademark, Copyright, & Brand Management Group for Halbrook & Pemberly's Seattle office. Curtis was also a senior associate at Silicon Valley based Thackery, Olmsted, Vance, & Bellweather."

Target Market(s)

Clients/potential clients needing tier one, international intellectual property advice with "mega" law firm experience for much less than what we were/would be charging at the "mega firms".

Industry/Entity Type

Legal

Number of Pages Required

4 page

Font styles to use
Serif
Sans Serif

Colors

Designer to choose colors to be used in the design.

Requirements
Must have
• +Improvement over everything on current site at www.tbkcounsel.com.
• +Pictures/bios for me and my team (four of us right now).
• +Easy to update and add/remove content.
• +Must be superior in design (look, feel, ease of use, classy and elegant, but hip, reflects international practice).
• +i have logos and color schemes (see current website) but will consider improvements.
Nice to have
• Let me know your thoughts.
Should not have
• No cheese; no overt sales pitches or marketing (since law firm).

```html
<!DOCTYPE html>
<html lang="en">
<head>
<meta charset="utf-8">
<title>TBK Law Group – Contact</title>
<link rel="stylesheet" href="https://fonts.googleapis.com/css2?family=Quattrocento:wght@400;700&family=Open+Sans:wght@400;600&display=swap">
<style>
:root{
  --orange:#f26f0f;
  --black:#000;
  --band:#f5f6f8;
  --field:#b5b5b5;
  --ink:#222;
  --muted:#8a8a8a;
  --logo:#7d7d7d;
  --white:#fff;
  --rule:#2a2a2a;
}
*{margin:0;padding:0;box-sizing:border-box}
html,body{width:1093px;height:1200px;overflow:hidden;background:var(--white)}
body{position:relative;font-family:'Quattrocento',serif;color:var(--ink)}
.abs{position:absolute}

.testimonials{left:0;top:0;width:1093px;height:127px;background:var(--band)}
.reviewer{position:absolute;top:20px;display:flex;align-items:center;gap:15px}
.reviewer .avatar{width:58px;height:58px;border-radius:50%;background:radial-gradient(circle at 50% 40%,#d9c7b8,#7b8a96)}
.reviewer .name{font-size:16px;color:var(--ink);margin-bottom:6px}
.reviewer .rating{font-family:'Open Sans',sans-serif;font-size:10.5px;color:#555;display:flex;align-items:center;gap:6px;letter-spacing:.5px}
.stars{display:flex;gap:2px}

.clients{left:0;top:127px;width:1093px;height:150px;background:var(--black);display:flex;align-items:center;justify-content:space-between;padding:0 118px}
.client{font-family:'Open Sans',sans-serif;font-weight:600;font-size:30px;color:var(--logo);display:flex;align-items:center;gap:8px}
.client .dot{width:26px;height:26px;border-radius:50%;background:var(--logo)}

.contact-title{left:0;width:1093px;top:310px;text-align:center;font-size:24px;letter-spacing:.5px}
.title-rule{left:509px;top:348px;width:63px;height:3px;background:var(--orange)}
.contact-lead{left:0;width:1093px;top:366px;text-align:center;font-size:21px;color:var(--muted)}
.contact-note{left:0;width:1093px;top:406px;text-align:center;font-size:14px;line-height:22px;color:var(--muted)}
.contact-note span{color:var(--ink)}

.field{background:var(--field);color:var(--white);font-size:15px;padding:0 21px;display:flex;align-items:center;letter-spacing:.3px}
.field.comment{align-items:flex-start;padding-top:12px}

.captcha{left:118px;top:715px;width:242px;height:60px;border:1px solid #d3d3d3;border-radius:3px;background:#f9f9f9;font-family:'Open Sans',sans-serif}
.captcha .box{position:absolute;left:10px;top:18px;width:22px;height:22px;border:2px solid #c1c1c1;border-radius:2px;background:var(--white)}
.captcha .label{position:absolute;left:42px;top:21px;font-size:11px;color:#222}
.captcha .mark{position:absolute;right:22px;top:9px;width:22px;height:22px;background:#9aa7c2}
.captcha .brand{position:absolute;right:10px;top:36px;font-size:7px;color:#777;text-align:center;line-height:11px}

.submit{left:493px;top:796px;width:95px;height:38px;background:var(--orange);border:2px solid #d45800;color:var(--white);font-size:12px;font-weight:700;letter-spacing:1px;display:flex;align-items:center;justify-content:center}

.footer{left:0;top:903px;width:1093px;height:297px;background:var(--black)}
.divider{position:absolute;top:0;width:1px;height:160px;background:var(--rule)}
.info{position:absolute;top:0;width:300px;text-align:center;color:var(--white)}
.info .badge{width:56px;height:56px;border-radius:50%;background:var(--orange);margin:-26px auto 0;display:flex;align-items:center;justify-content:center}
.info h3{font-weight:400;font-size:21px;margin-top:18px}
.info p{font-family:'Open Sans',sans-serif;font-size:13.5px;line-height:22px;color:#b0b0b0;margin-top:6px}
.info p.big{font-size:17px}
.social{display:flex;justify-content:center;gap:24px;margin-top:16px}
.social span{width:14px;height:14px;border-radius:50%;background:var(--white)}
.nav{position:absolute;left:0;top:160px;width:1093px;height:48px;border-top:1px solid var(--rule);border-bottom:1px solid var(--rule);display:flex;justify-content:center;align-items:center;gap:46px;font-size:13px;color:#bbb;letter-spacing:.5px}
.nav .current{color:var(--orange)}
.copyright{position:absolute;left:0;top:234px;width:1093px;text-align:center;font-size:11px;color:#999}
</style>
</head>
<body>

<section class="abs testimonials">
  <div class="reviewer" style="left:131px">
    <div class="avatar" role="img" aria-label="Portrait photo of client Walter Brennick"></div>
    <div><div class="name">Walter Brennick</div><div class="rating">Reviews: <span class="stars" aria-label="5 stars"></span></div></div>
  </div>
  <div class="reviewer" style="left:428px">
    <div class="avatar" role="img" aria-label="Portrait photo of client Selena Marchetti"></div>
    <div><div class="name">Selena Marchetti</div><div class="rating">Reviews: <span class="stars" aria-label="5 stars"></span></div></div>
  </div>
  <div class="reviewer" style="left:725px">
    <div class="avatar" role="img" aria-label="Portrait photo of client Damon Ashcroft"></div>
    <div><div class="name">Damon Ashcroft</div><div class="rating">Reviews: <span class="stars" aria-label="5 stars"></span></div></div>
  </div>
</section>
<style>
.stars::before{content:"★★★★★";color:var(--orange);font-size:13px;letter-spacing:1px}
</style>

<section class="abs clients" aria-label="Clients">
  <div class="client"><span class="dot"></span>Norvale</div>
  <div class="client">Crestline Partners</div>
  <div class="client">Orchard</div>
  <div class="client">Veltrix</div>
  <div class="client"><span class="dot"></span>Farway</div>
</section>

<h2 class="abs contact-title">CONTACT INFO</h2>
<div class="abs title-rule"></div>
<p class="abs contact-lead">Do you have question? We can help!</p>
<p class="abs contact-note">To speak to our member, please call us at <span>206.555.0148</span>&nbsp; or e-mail us at <span>contact@tbklawgroup.com</span>.<br>You can also contact us by filling out the following form:</p>

<div class="abs field" style="left:117px;top:486px;width:418px;height:40px">First Name</div>
<div class="abs field" style="left:558px;top:486px;width:418px;height:40px">Last Name</div>
<div class="abs field" style="left:117px;top:542px;width:418px;height:40px">Email Address</div>
<div class="abs field" style="left:558px;top:542px;width:418px;height:40px">Phone Number</div>
<div class="abs field comment" style="left:117px;top:599px;width:859px;height:104px">Comment</div>

<div class="abs captcha">
  <div class="box"></div>
  <div class="label">I'm not a robot</div>
  <div class="mark"></div>
  <div class="brand">HumanCheck<br>Privacy - Terms</div>
</div>

<div class="abs submit">SUBMIT</div>

<footer class="abs footer">
  <div class="divider" style="left:402px"></div>
  <div class="divider" style="left:685px"></div>

  <div class="info" style="left:105px">
    <div class="badge"><svg width="22" height="28" viewBox="0 0 22 28"><path d="M11 2a8 8 0 0 0-8 8c0 6 8 15 8 15s8-9 8-15a8 8 0 0 0-8-8z" fill="none" stroke="#fff" stroke-width="2"/><circle cx="11" cy="10" r="3" fill="none" stroke="#fff" stroke-width="2"/></svg></div>
    <h3>Address</h3>
    <p>240 W. 41st St. Suite C. Seattle<br>WA. 98107</p>
  </div>
  <div class="info" style="left:391px">
    <div class="badge"><svg width="22" height="24" viewBox="0 0 22 24"><path d="M6 2l4 5-2 3c1 3 3 5 6 6l3-2 4 4-3 3C10 21 3 13 3 5z" fill="#fff"/></svg></div>
    <h3>Phone</h3>
    <p class="big">206.555.0148</p>
  </div>
  <div class="info" style="left:672px">
    <div class="badge"><svg width="24" height="18" viewBox="0 0 24 18"><rect x="2" y="2" width="20" height="14" fill="none" stroke="#fff" stroke-width="1.6"/><path d="M2 2l10 8 10-8M2 16l7-6M22 16l-7-6" fill="none" stroke="#fff" stroke-width="1.6"/></svg></div>
    <h3>Email</h3>
    <p>contact@tbklawgroup.com</p>
    <div class="social" aria-label="Social links"><span></span><span></span><span></span><span></span></div>
  </div>

  <nav class="nav">
    <span class="current">HOME</span><span>/</span><span>EXPERIENCE</span><span>/</span><span>ABOUT</span><span>/</span><span>CONTACT</span>
  </nav>
  <p class="copyright">© 2008-2010 TBK LAW GROUP PLLC &nbsp;|&nbsp; All Rights Reserved.</p>
</footer>

</body>
</html>
```